Logo design and Businesscard and letterhead for Technology Company

We need logo design for a new company based in Atlanta called "Vornimel". We provide information about technology Product and service provider companies, information about their Products and services. Our initial focus is to List various companies and their products, various consulting companies and their services. We want to convey the message that this will be one stop shop to find out all the information to make smart technology decisions

I am looking for Logo, Business Card and Letterhead.

Target Market(s)

Companies that have IT department, IT users such as Developers, Managers, C level, Technology Product companies , Consulting companies and service providers.

Industry/Entity Type

It Company

Requirements
Must have
• Looking for some Unique design idea.
Nice to have
• I want something that connects information across technologies between technology buyers and sellers.
Should not have
• No puzzle design.

```html
<!DOCTYPE html>
<html lang="en">
<head>
<meta charset="utf-8">
<title>Vornimel Letterhead</title>
<link rel="stylesheet" href="https://fonts.googleapis.com/css2?family=Lexend:wght@400;500;600&display=swap">
<style>
  :root {
    --navy: #14307f;
    --green: #8dbb1a;
    --ink: #1a1a1a;
    --paper: #ffffff;
    --band-a: #1f2d8f;
    --band-b: #003a7c;
    --band-c: #0a5e92;
    --band-d: #0b1a3e;
    --band-e: #1b2862;
  }
  html, body {
    margin: 0;
    padding: 0;
    overflow: hidden;
    background: var(--paper);
  }
  .sheet {
    position: relative;
    width: 1002px;
    height: 1200px;
    background: var(--paper);
    font-family: "Lexend", sans-serif;
    overflow: hidden;
  }
  .print-marks {
    position: absolute;
    inset: 0;
  }
  .brand {
    position: absolute;
    left: 154px;
    top: 148px;
    margin: 0;
  }
  .brand-name {
    font-size: 44px;
    font-weight: 600;
    color: var(--green);
    line-height: 1;
    letter-spacing: -0.5px;
  }
  .contact {
    position: absolute;
    right: 167px;
    top: 142px;
    text-align: right;
    font-style: normal;
    font-size: 12.2px;
    line-height: 17.5px;
    color: var(--navy);
  }
  .contact .label {
    color: var(--green);
  }
  .contact p {
    margin: 0;
  }
  .footer-band {
    position: absolute;
    left: 111px;
    top: 996px;
    width: 776px;
    height: 99px;
    background:
      linear-gradient(160deg, transparent 40%, rgba(10, 94, 146, 0.55) 60%, transparent 80%),
      linear-gradient(100deg, var(--band-a) 0%, var(--band-b) 18%, var(--band-c) 32%, var(--band-d) 45%, var(--band-b) 60%, var(--band-c) 72%, var(--band-a) 84%, var(--band-e) 100%);
  }
</style>
</head>
<body>
<div class="sheet">
  <svg class="print-marks" width="1002" height="1200" viewBox="0 0 1002 1200" aria-hidden="true">
    <g stroke="var(--ink)" stroke-width="0.6" fill="none">
      <line x1="122" y1="43" x2="122" y2="101"/>
      <line x1="876" y1="43" x2="876" y2="101"/>
      <line x1="57" y1="108" x2="116" y2="108"/>
      <line x1="885" y1="108" x2="944" y2="108"/>
      <line x1="55" y1="1085" x2="113" y2="1085"/>
      <line x1="887" y1="1085" x2="942" y2="1085"/>
      <line x1="122" y1="1095" x2="122" y2="1151"/>
      <line x1="876" y1="1095" x2="876" y2="1151"/>
    </g>
    <g class="registration" stroke="var(--ink)" stroke-width="0.7" fill="none">
      <g transform="translate(499 66)"><circle r="6.5"/><line x1="-9" y1="0" x2="9" y2="0"/><line x1="0" y1="-9" x2="0" y2="9"/><circle r="3.5" fill="var(--ink)"/></g>
      <g transform="translate(86 593)"><circle r="6.5"/><line x1="-9" y1="0" x2="9" y2="0"/><line x1="0" y1="-9" x2="0" y2="9"/><circle r="3.5" fill="var(--ink)"/></g>
      <g transform="translate(912 593)"><circle r="6.5"/><line x1="-9" y1="0" x2="9" y2="0"/><line x1="0" y1="-9" x2="0" y2="9"/><circle r="3.5" fill="var(--ink)"/></g>
      <g transform="translate(499 1127)"><circle r="6.5"/><line x1="-9" y1="0" x2="9" y2="0"/><line x1="0" y1="-9" x2="0" y2="9"/><circle r="3.5" fill="var(--ink)"/></g>
    </g>
  </svg>

  <header class="brand">
    <span class="brand-name">Vornimel</span>
  </header>

  <address class="contact">
    <p>48 Larkspur Ridge Rd, Marlow Park, GA 30412</p>
    <p><span class="label">Phone:</span> 404 555 0187 <span class="label">Email:</span> info@vornimel.com</p>
    <p><span class="label">W:</span> www.vornimel.com</p>
  </address>

  <div class="footer-band" role="img" aria-label="Deep blue footer band with sweeping light streaks and a circuit-board line pattern"></div>
</div>
</body>
</html>
```